Looking for a professional, clean and crisp business card

I am in the underground utilities industry and am just looking for a really impressive business card. I would like our card to be white with our symbol crisp and clear with it protruding. I also have a business partner that will require his name and info on the card once the design is set. I would like to have our website info on the card which is;
http://granitetrenchco.example/

Contact Information for Business Card

Website, contact name, number and email

```html
<!DOCTYPE html>
<html lang="en">
<head>
<meta charset="UTF-8">
<title>Granite Trench Co — Business Card</title>
<link href="https://fonts.googleapis.com/css2?family=Lato:wght@400;700;900&display=swap" rel="stylesheet">
<style>
  :root {
    --page-bg: #e9e9e7;
    --card-white: #ffffff;
    --card-dark: #1c1d20;
    --card-dark-edge: #2b2c30;
    --ink: #4a4a4a;
    --ink-strong: #3c3c3c;
    --accent-blue: #4a7fc1;
    --rule: #8a8a8a;
  }
  * { box-sizing: border-box; margin: 0; padding: 0; }
  html, body {
    width: 1200px; height: 1200px; overflow: hidden;
    background: var(--page-bg);
    font-family: "Lato", sans-serif;
  }
  .canvas {
    width: 1200px; height: 1200px;
    display: flex; flex-direction: column;
    align-items: center; justify-content: center; gap: 44px;
  }
  .card {
    width: 900px; height: 514px;
    position: relative;
    box-shadow: 0 6px 18px rgba(0,0,0,0.18);
  }
  /* Back side */
  .card--back {
    background: linear-gradient(120deg, var(--card-dark) 0%, var(--card-dark) 55%, var(--card-dark-edge) 100%);
    display: flex; flex-direction: column; align-items: center; justify-content: center;
  }
  .brand {
    display: flex; align-items: center; gap: 18px;
    font-weight: 900; letter-spacing: 1px; text-transform: uppercase;
  }
  .brand__dot { border-radius: 50%; flex: none; }
  .card--back .brand { color: var(--card-white); font-size: 46px; }
  .card--back .brand__dot { width: 40px; height: 40px; background: var(--accent-blue); }
  .back__web {
    margin-top: 70px;
    color: var(--accent-blue); font-size: 30px; letter-spacing: 1px;
  }
  /* Front side */
  .card--front {
    background: var(--card-white);
    display: flex; align-items: center;
    padding: 0 60px;
  }
  .front__brand-area { width: 300px; display: flex; justify-content: center; }
  .card--front .brand { color: var(--ink-strong); font-size: 30px; gap: 12px; flex-direction: column; text-align: center; }
  .card--front .brand__dot { width: 30px; height: 30px; background: var(--accent-blue); }
  .front__rule { width: 2px; height: 270px; background: var(--rule); margin: 0 50px 0 20px; }
  .contact__name { font-size: 38px; font-weight: 700; color: var(--ink); margin-bottom: 22px; }
  .contact__list { list-style: none; }
  .contact__item {
    display: flex; align-items: center; gap: 20px;
    font-size: 30px; color: var(--ink); letter-spacing: 1px;
    margin-bottom: 12px;
  }
  .contact__icon { width: 28px; height: 28px; flex: none; }
</style>
</head>
<body>
<main class="canvas">
  <section class="card card--back" aria-label="Card back">
    <div class="brand"><span class="brand__dot"></span><span>Granite Trench Co</span></div>
    <p class="back__web">www.granitetrenchco.example</p>
  </section>

  <section class="card card--front" aria-label="Card front">
    <div class="front__brand-area">
      <div class="brand"><span class="brand__dot"></span><span>Granite<br>Trench Co</span></div>
    </div>
    <div class="front__rule"></div>
    <div class="contact">
      <p class="contact__name">Person Name</p>
      <ul class="contact__list">
        <li class="contact__item">
          <svg class="contact__icon" viewBox="0 0 24 24" fill="none" stroke="#4a7fc1" stroke-width="2"><rect x="6" y="2" width="12" height="20" rx="2"/><line x1="10" y1="18" x2="14" y2="18"/></svg>
          <span>555-014-2290</span>
        </li>
        <li class="contact__item">
          <svg class="contact__icon" viewBox="0 0 24 24" fill="none" stroke="#4a7fc1" stroke-width="2"><rect x="2" y="5" width="20" height="14" rx="1"/><polyline points="2,6 12,13 22,6"/></svg>
          <span>info@granitetrenchco.example</span>
        </li>
        <li class="contact__item">
          <svg class="contact__icon" viewBox="0 0 24 24" fill="none" stroke="#4a7fc1" stroke-width="2"><circle cx="12" cy="12" r="10"/><ellipse cx="12" cy="12" rx="4.5" ry="10"/><line x1="2" y1="12" x2="22" y2="12"/></svg>
          <span>www.granitetrenchco.example</span>
        </li>
      </ul>
    </div>
  </section>
</main>
</body>
</html>
```